The Brightwater Compass Business Card

We need an attractive business card with the logo that we bought from ArtVantly last year.
Our mission is to contribute to change the way today's leaders manage business companies bringing value to the workplace and helping them to build a new model of creating wealth.
Our logo is clear about our values : we seek Positive Change through People and are convinced that the pursuit of individual well-being and the chase of economic results can converge with the right management.
Management Consulting
Corinne Fabrelle
+34 612 98 70 31
corinne.fabrelle@thebrightwatercompass-mail.net
www.thebrightwatercompass-mail.net

```html
<!DOCTYPE html>
<html lang="en">
<head>
<meta charset="utf-8">
<title>The Brightwater Compass Business Card</title>
<link href="https://fonts.googleapis.com/css2?family=Cinzel:wght@400;600&family=Arimo:wght@400&display=swap" rel="stylesheet">
<style>
  :root {
    --canvas: #e9e7e3;
    --paper: #f7f7f6;
    --brand-green: #559c86;
    --brand-teal: #3f8f77;
    --brand-deep: #2f6c5c;
    --stripe: #a9d6c7;
    --mist: #dcdfdf;
    --white: #ffffff;
  }
  * { margin: 0; padding: 0; box-sizing: border-box; }
  html, body { width: 1200px; height: 842px; overflow: hidden; }
  body {
    background: var(--canvas);
    display: flex;
    flex-direction: column;
    align-items: center;
    justify-content: center;
    gap: 56px;
  }
  .card {
    position: relative;
    width: 600px;
    height: 343px;
    overflow: hidden;
    box-shadow: 0 6px 18px rgba(0,0,0,0.15);
  }

  /* Front */
  .card-front { background: var(--paper); }
  .tree-decoration {
    position: absolute;
    left: 330px; top: 8px;
    width: 260px; height: 150px;
    border-radius: 50% 50% 40% 40%;
    background: radial-gradient(ellipse at 50% 45%, var(--mist) 0%, rgba(220,223,223,0.55) 55%, rgba(220,223,223,0) 75%);
  }
  .wave { position: absolute; inset: 0; width: 600px; height: 343px; }
  .holder-name {
    position: absolute; left: 40px; top: 112px;
    font-family: "Cinzel", serif; font-weight: 600;
    font-size: 25px; letter-spacing: 0.5px;
    color: var(--brand-teal);
  }
  .contact {
    position: absolute; left: 42px; top: 150px;
    font-family: "Arimo", sans-serif; font-size: 12.5px; line-height: 17px;
    color: var(--brand-teal);
  }
  .front-mark {
    position: absolute; left: 40px; top: 208px;
    display: flex; align-items: center; gap: 8px;
    font-family: "Cinzel", serif; font-weight: 600; font-size: 14px;
    line-height: 18px;
    color: var(--brand-deep);
    white-space: nowrap;
  }
  .front-mark .dot { width: 11px; height: 11px; border-radius: 50%; background: var(--brand-deep); flex: none; }
  .front-web {
    position: absolute; right: 28px; bottom: 60px;
    font-family: "Arimo", sans-serif; font-size: 12px;
    color: var(--white);
  }

  /* Back */
  .card-back {
    background: var(--brand-green);
    display: flex; flex-direction: column; align-items: center; justify-content: center;
    color: var(--white);
  }
  .back-mark {
    font-family: "Cinzel", serif; font-weight: 600; font-size: 36px;
    letter-spacing: 1px; color: var(--white);
  }
  .back-rule {
    width: 360px; height: 1px; background: var(--white); opacity: 0.8; margin: 14px 0 12px;
  }
  .back-web { font-family: "Arimo", sans-serif; font-size: 14px; color: var(--white); }
</style>
</head>
<body>

  <section class="card card-front">
    <div class="tree-decoration" role="img" aria-label="Faint grey tree decoration"></div>
    <svg class="wave" viewBox="0 0 600 343" aria-hidden="true">
      <path d="M0 322 C160 318 300 262 420 172 C480 128 540 112 600 108 L600 122 C540 126 482 142 424 184 C304 272 160 330 0 334 Z" fill="var(--stripe)"/>
      <path d="M0 336 C160 332 304 278 426 190 C484 148 542 132 600 128 L600 343 L0 343 Z" fill="var(--brand-green)"/>
    </svg>
    <h1 class="holder-name">Corinne Fabrelle</h1>
    <p class="contact">+34 612 98 70 31<br>corinne.fabrelle@thebrightwatercompass-mail.net</p>
    <div class="front-mark"><span class="dot"></span>The Brightwater Compass</div>
    <p class="front-web">www.thebrightwatercompass-mail.net</p>
  </section>

  <section class="card card-back">
    <div class="back-mark">The Brightwater Compass</div>
    <div class="back-rule"></div>
    <p class="back-web">www.thebrightwatercompass-mail.net</p>
  </section>

</body>
</html>
```